Jewelry store needs fully functional Ecommerce website

Web Design Brief for our E-commerce Jewelry retail store.
Description

We need a fully coded Shopify website. The Shopify site will need to be fully functional with an Ecommerce integration (fully integrated with Paypal and All other gateways) and will need to be SEO optimized.
We sell jewelry items like: rings, earrings, necklaces etc. The website should have an elegant, modern, professional, fun, look.

***We would like the website to look and function similarly to this website:
https://velvorisco.com

Color Preference
Colors to be used are white background with black font and light pink/ purple/ gold tints. We have attached our logo as reference.

Functionalities
The store will function like a typical Ecommerce jewelry store, using the products/categories as the starting page. Going into individual product pages by selecting images and leading to a detailed “buy now” page for the selected product.

Target Market
Jewelry lovers.

Should Not Have:
- - Dull and common design
- - Messy/unstructured navigation

Coded - Design and coding required
Target Audience are women from 16-50 years old.
We will need to be able to add products and make modifications to the website as needed.

We need the following apps installed and Operating:
-Tally Shift; Order Look Up (rename “track your order”) ; Help Center (Questions and Answers) ; Pemmo Reviews; TXT Nudge; Drenoza Email Marketing ; Plivet (Facebook messenger bump) ; Vantro multi- currency (translate currency to buyer) ; Discounted Upsell ; Easy Contact form App
We will need all products imported: (below is information for importing products). We will provide all links that serve entire active item product catalog in shopifys import format:
DataFeed:

If you are getting started with Shopify, a combination of the Shopify Import Format and XML feeds is ideal. The Shopify Import Format will output a file that can be uploaded into Shopify’s product database. After you import, you can use the XML feed and a third party app to keep the inventory up to date in real time, take down items that go out of stock etc., all without regular human intervention. There a several Shopify apps that can do this type of feed integration. We have had a good experience with Tally Shift, which is an app that can be configured to accept our XML feed and update products on a set schedule. You can even set your own margins based on our wholesale price with this app.

Shopify Formatted HTML TableTo make it easier to get started on Shopify, we included a format that outputs the required fields for a product import in Shopify. In order to use the embedded Excel file, first open the file (Auto-Shopify-Datasheet-Format.xslx), Refresh it (under Data tab), and then Save As with a new file name in a CSV (UTF-8) file. That file can then be split into smaller CSV files (if there is a limit on the number of products per file) for import into Shopify.

Target Market(s)

Jewelry Lovers

Industry/Entity Type

Jewelry Store

Coding

Number of Pages Required

5+ page

Colors
eda3c7
d3a5cc
ffffff

Requirements
Must have
• Color Preference
Colors to be used are white background with black font and light pink/ purple/ gold tints.

https://velvorisco.com
Should not have
• Should Not Have:

```html
<!DOCTYPE html>
<html lang="en">
<head>
<meta charset="utf-8">
<title>Ever Belle — Jewelry Collection</title>
<link href="https://fonts.googleapis.com/css2?family=Raleway:wght@400;500;600;700&family=Hind:wght@300;400;500;600&display=swap" rel="stylesheet">
<style>
:root{
  --gold:#c99a34;
  --gold-text:#c9962e;
  --ink:#111111;
  --grey-text:#8a8a8a;
  --sand:#f6e1c7;
  --mist:#f2f5f8;
  --stone:#e9e9e9;
  --haze:#f4f3f4;
  --navy:#10284a;
  --white:#ffffff;
}
*{box-sizing:border-box;margin:0;padding:0}
html,body{width:1200px;height:3000px;overflow:hidden;background:var(--white)}
body{position:relative;font-family:"Raleway",sans-serif;color:var(--ink)}
.abs{position:absolute}
.heading{font-family:"Hind",sans-serif}
.btn{position:absolute;display:flex;align-items:center;justify-content:center;border:2px solid var(--ink);font-family:"Hind",sans-serif;font-weight:600;font-size:16px;letter-spacing:.8px;color:var(--ink);background:transparent}
.btn.light{border-color:var(--white);color:var(--white)}
.photo{position:absolute}

/* header */
.brand{left:92px;top:28px;font-size:30px;font-weight:500;color:var(--ink);letter-spacing:1px}
.nav-icons{left:870px;top:22px;width:260px;height:30px}

/* hero */
.hero-circle{left:512px;top:-76px;width:686px;height:686px;border-radius:50%;background:#d4d9d8}
.hero-photo{left:478px;top:85px;width:722px;height:628px;border-radius:360px 0 0 0;background:linear-gradient(150deg,#e9c7a6 0%,#d9a57f 45%,#b97e5a 100%)}
.hero-kicker{left:86px;top:280px;font-size:45px;font-weight:600;color:var(--gold-text);letter-spacing:1px}
.hero-title{left:86px;top:330px;font-size:46px;font-weight:600;letter-spacing:1.5px}
.hero-copy{left:89px;top:394px;width:420px;font-size:15px;line-height:21px}

/* categories */
.cat{position:absolute;top:716px;height:385px;text-align:center}
.cat-1{left:0;width:394px;background:var(--stone)}
.cat-2{left:394px;width:411px;background:var(--gold)}
.cat-3{left:805px;width:395px;background:#ececec}
.cat-img{position:absolute;top:50px;left:50%;transform:translateX(-50%);width:170px;height:150px;border-radius:50%}
.cat-title{position:absolute;top:226px;left:0;right:0;font-family:"Hind",sans-serif;font-weight:600;font-size:18px;letter-spacing:.8px}
.cat-copy{position:absolute;top:256px;left:50%;transform:translateX(-50%);width:290px;font-size:13.5px;line-height:17px;color:var(--grey-text)}
.cat-2 .cat-title,.cat-2 .cat-copy{color:var(--white)}

/* women's bands */
.bands{left:0;top:1101px;width:1200px;height:399px;background:var(--mist)}
.bands-title{left:97px;top:1230px;font-size:27px;font-weight:600;letter-spacing:1.2px}
.bands-copy{left:97px;top:1276px;width:310px;font-size:15px;line-height:21px}

/* couples */
.couples{left:0;top:1500px;width:730px;height:403px;background:var(--sand)}
.offer{left:730px;top:1500px;width:470px;height:403px;background:var(--gold);color:var(--white);text-align:center}
.couples-line{left:97px;top:1540px;font-size:21px;letter-spacing:.8px;font-family:"Hind",sans-serif}
.couples-line b{color:var(--navy);font-weight:600}
.design-a{left:380px;top:1648px;width:330px;text-align:center;font-family:"Hind",sans-serif;font-size:28px;font-weight:300;letter-spacing:1px}
.design-b{left:380px;top:1682px;width:330px;text-align:center;font-family:"Hind",sans-serif;font-size:32px;font-weight:600;letter-spacing:1.5px}
.arrow{position:absolute;top:1520px;width:34px;height:34px;border:1px solid var(--white);border-radius:3px}
.offer-title{position:absolute;top:236px;left:0;right:0;font-family:"Hind",sans-serif;font-weight:600;font-size:20px;letter-spacing:.8px}
.offer-copy{position:absolute;top:268px;left:50%;transform:translateX(-50%);width:300px;font-size:14px;line-height:17px}
.offer-price{position:absolute;top:333px;left:0;right:0;font-family:"Hind",sans-serif;font-size:31px;font-weight:500}

/* stories */
.stories{left:0;top:1903px;width:1200px;height:405px;background:var(--haze)}
.stories-head{left:80px;top:2006px;width:500px;text-align:center;font-size:22px;line-height:25px;font-weight:500}
.quote{left:120px;top:2090px;width:420px;text-align:center;font-size:16px;line-height:18px}
.qmark{position:absolute;font-family:"Hind",sans-serif;font-size:30px;line-height:1}
.cite{left:80px;top:2158px;width:480px;text-align:center;font-size:12px;color:var(--grey-text)}
.stories-link{left:265px;top:2210px;font-size:12px;text-decoration:underline;color:#333}

/* features */
.feature-icon{position:absolute;top:2361px;width:84px;height:84px;border-radius:50%;background:var(--sand)}
.feature-title{position:absolute;top:2370px;font-family:"Hind",sans-serif;font-weight:600;font-size:16px;letter-spacing:.8px}
.feature-copy{position:absolute;top:2396px;width:210px;font-size:12.5px;line-height:17px;color:var(--grey-text)}

/* newsletter */
.newsletter{left:0;top:2527px;width:1200px;height:72px;background:#e5e5e5}
.nl-label{left:148px;top:2553px;font-size:15px;font-weight:500}
.nl-input{left:410px;top:2544px;width:425px;height:38px;background:var(--white);border:1px solid #dcdcdc;font-size:14px;color:#aaa;padding:10px 14px}
.nl-btn{left:855px;top:2544px;width:163px;height:38px;background:var(--navy);color:var(--white);font-size:15px;font-weight:500;display:flex;align-items:center;justify-content:center}

/* footer */
.footer{left:0;top:2599px;width:1200px;height:401px;background:#f4f4f4}
.f-col{position:absolute;top:2646px}
.f-col h4{font-size:11.5px;font-weight:700;color:var(--navy);letter-spacing:.5px;margin-bottom:14px}
.f-col li{list-style:none;font-size:11.5px;color:#555;line-height:20.6px;letter-spacing:.3px}
.social{position:absolute;top:2849px;width:26px;height:26px;border-radius:50%}
.pay{position:absolute;top:2851px;width:44px;height:24px;border-radius:3px;background:#c5c5c5}
.badge{left:978px;top:2849px;width:104px;height:28px;border:1px solid #aaa;background:#ececec}
.legal{left:0;top:2910px;width:1200px;text-align:center;font-size:12px;line-height:19px;color:#333}
.legal b{font-weight:700}
</style>
</head>
<body>

<header>
  <div class="abs brand">Ever Belle</div>
  <svg class="abs nav-icons" viewBox="0 0 260 30" fill="none" stroke="#222" stroke-width="1.6" aria-label="Site navigation">
    <circle cx="13" cy="13" r="8"/><line x1="19" y1="19" x2="25" y2="25"/>
    <circle cx="66" cy="9" r="5"/><path d="M57 24c0-6 4-9 9-9s9 3 9 9z"/>
    <path d="M122 25l-10-10a6 6 0 0 1 10-7 6 6 0 0 1 10 7z"/>
    <path d="M172 10h14l2 16h-18z"/><path d="M175 10a4 4 0 0 1 8 0"/>
    <circle cx="187" cy="27" r="3" fill="#e06a6a" stroke="none"/>
    <line x1="220" y1="9" x2="240" y2="9"/><line x1="220" y1="14" x2="240" y2="14"/><line x1="220" y1="19" x2="240" y2="19"/>
  </svg>
</header>

<section class="hero">
  <div class="abs hero-circle"></div>
  <div class="photo hero-photo" role="img" aria-label="Close-up photograph of a woman wearing gold rings and a fine gold necklace"></div>
  <div class="abs heading hero-kicker">FROM $299</div>
  <h1 class="abs heading hero-title">JEWELRY COLLECTION</h1>
  <p class="abs hero-copy">Aenean sollicitudin, lorem quis bibendum auctor, nisi elit consequat ipsum, nec sagittis sem nibh id elit. Duis sed odio sit amet nibh</p>
  <div class="btn" style="left:86px;top:471px;width:118px;height:40px">SHOP NOW</div>
</section>

<section class="categories">
  <div class="cat cat-1">
    <div class="cat-img" role="img" aria-label="Silver engagement ring with a violet gemstone" style="background:radial-gradient(circle at 50% 30%,#5b4bb8 0 22%,#d9d9d9 23%,#bdbdbd 60%,var(--stone) 70%)"></div>
    <div class="cat-title">HEIRLOOM ENGAGEMENT RINGS</div>
    <p class="cat-copy">Accordingly composed pictures in which contrived to get as many lines as possible leading inward</p>
    <div class="btn" style="left:183px;top:324px;width:122px;height:38px">LEARN MORE</div>
  </div>
  <div class="cat cat-2">
    <div class="cat-img" role="img" aria-label="Three diamond wedding band rings" style="width:250px;border-radius:40%;background:radial-gradient(ellipse at 50% 50%,#f0f0f0 0 30%,#cfcfcf 45%,var(--gold) 70%)"></div>
    <div class="cat-title">HEIRLOOM WEDDING BANDS</div>
    <p class="cat-copy">Accordingly composed pictures in which contrived to get as many lines as possible leading inward</p>
    <div class="btn light" style="left:152px;top:324px;width:122px;height:38px">LEARN MORE</div>
  </div>
  <div class="cat cat-3">
    <div class="cat-img" role="img" aria-label="Violet gemstone jewel set in diamonds" style="background:radial-gradient(circle at 50% 40%,#4b3ea8 0 24%,#d4d4d4 30%,#bdbdbd 50%,#ececec 68%)"></div>
    <div class="cat-title">HEIRLOOM FINE JEWELRY</div>
    <p class="cat-copy">Accordingly composed pictures in which contrived to get as many lines as possible leading inward</p>
    <div class="btn" style="left:91px;top:324px;width:122px;height:38px">LEARN MORE</div>
  </div>
</section>

<section>
  <div class="abs bands"></div>
  <h2 class="abs heading bands-title">WOMEN’S WEDDING BANDS</h2>
  <p class="abs bands-copy">Accordingly composed pictures in which contrived to get as many lines as possible leading inward</p>
  <div class="btn" style="left:97px;top:1357px;width:122px;height:40px">SHOP NOW</div>
  <div class="photo" role="img" aria-label="Gold crown ornament topped with a red-stone cross" style="left:600px;top:1130px;width:235px;height:370px;border-radius:45% 45% 8px 8px;background:linear-gradient(180deg,#e8c868,#c99a34 60%,#efe6d0 92%)"></div>
  <div class="photo" role="img" aria-label="Gold and silver interlocking heart pendant on a gold chain" style="left:860px;top:1101px;width:340px;height:370px;border-radius:50% 50% 45% 45%;background:radial-gradient(ellipse at 45% 55%,#d8d8d8 0 18%,#f0cf5a 30%,var(--mist) 62%)"></div>
</section>

<section>
  <div class="abs couples"></div>
  <div class="abs couples-line">150,000 HAPPY <b>COUPLES</b> &amp; COUNTING</div>
  <div class="photo" role="img" aria-label="Pair of pavé diamond hoop earrings" style="left:87px;top:1595px;width:278px;height:235px;border-radius:40%;background:radial-gradient(ellipse,#ececec 0 35%,#c9c9c9 55%,var(--sand) 72%)"></div>
  <div class="abs design-a">DESIGN YOUR OWN</div>
  <div class="abs design-b">ENGAGEMENT RING</div>
  <div class="btn" style="left:478px;top:1749px;width:122px;height:40px">SHOP NOW</div>

  <div class="abs offer">
    <div class="offer-title">LOREM COLLECTIONS</div>
    <p class="offer-copy">Accordingly composed pictures in which contrived to get as many lines as possible leading inward</p>
    <div class="offer-price">$ 299</div>
  </div>
  <svg class="arrow" style="left:745px" viewBox="0 0 34 34" aria-label="Previous"><path d="M19 11l-6 6 6 6" fill="none" stroke="#fff" stroke-width="1.6"/></svg>
  <svg class="arrow" style="left:784px" viewBox="0 0 34 34" aria-label="Next"><path d="M15 11l6 6-6 6" fill="none" stroke="#fff" stroke-width="1.6"/></svg>
  <div class="photo" role="img" aria-label="Diamond engagement ring with matching band" style="left:855px;top:1548px;width:180px;height:165px;border-radius:50%;background:radial-gradient(circle,#f4f4f4 0 25%,#d2d2d2 45%,var(--gold) 70%)"></div>
</section>

<section>
  <div class="abs stories"></div>
  <div class="photo" role="img" aria-label="Photograph of a smiling young woman outdoors wearing rings" style="left:800px;top:1903px;width:400px;height:405px;background:linear-gradient(100deg,var(--haze) 0%,#6f7a55 18%,#4e5a3a 45%,#c99a80 75%,#b78468 100%)"></div>
  <h3 class="abs stories-head">View our customers' engagement moments from around the world</h3>
  <span class="qmark" style="left:112px;top:2083px">“</span>
  <p class="abs quote">...Eventually, we came upon a secluded gazebo, and the rest was history...</p>
  <span class="qmark" style="left:446px;top:2130px">”</span>
  <p class="abs cite">- Nadia Ferrell (California, US)</p>
  <div class="abs stories-link">READ THE STORIES</div>
</section>

<section>
  <div class="feature-icon" style="left:86px"></div>
  <svg class="abs" style="left:108px;top:2380px" width="40" height="46" viewBox="0 0 40 46" fill="none" stroke="#444" stroke-width="1.4" aria-label="Shipping icon"><path d="M20 3C9 3 4 11 4 18c0 8 8 15 13 20h6c5-5 13-12 13-20 0-7-5-15-16-15z"/><path d="M20 3c-5 4-7 10-7 16s2 14 4 19M20 3c5 4 7 10 7 16s-2 14-4 19"/><rect x="16" y="38" width="8" height="5"/></svg>
  <div class="feature-title" style="left:186px">FREE SHIPPING</div>
  <p class="feature-copy" style="left:186px">But from the first I was disap-pointed with it. In about a week I was tired of seeing sights</p>

  <div class="feature-icon" style="left:440px"></div>
  <svg class="abs" style="left:458px;top:2385px" width="48" height="36" viewBox="0 0 48 36" fill="none" stroke="#444" stroke-width="1.4" aria-label="Wallet icon"><path d="M4 8l30-6 2 6"/><rect x="3" y="8" width="40" height="26" rx="2"/><rect x="32" y="16" width="11" height="9"/><circle cx="37" cy="20.5" r="1.5"/></svg>
  <div class="feature-title" style="left:543px">REFUND OPTION</div>
  <p class="feature-copy" style="left:543px">I had no real pal to go about with, which probably explains things. Plenty of people invited me</p>

  <div class="feature-icon" style="left:793px"></div>
  <svg class="abs" style="left:813px;top:2382px" width="44" height="42" viewBox="0 0 44 42" fill="none" stroke="#444" stroke-width="1.4" aria-label="Payment options icon"><ellipse cx="22" cy="21" rx="19" ry="7"/><ellipse cx="22" cy="21" rx="19" ry="7" transform="rotate(60 22 21)"/><ellipse cx="22" cy="21" rx="19" ry="7" transform="rotate(-60 22 21)"/><circle cx="22" cy="21" r="2.5"/></svg>
  <div class="feature-title" style="left:893px">PAYMENT OPTIONS</div>
  <p class="feature-copy" style="left:893px">They would fling me a question or two about South Africa, and then get on their own affairs</p>
</section>

<section>
  <div class="abs newsletter"></div>
  <div class="abs nl-label">SIGN UP FOR OUR NEWSLETTER</div>
  <div class="abs nl-input">Enter Your Email</div>
  <div class="abs nl-btn">SUBSCRIBE NOW</div>
</section>

<footer>
  <div class="abs footer"></div>
  <div class="f-col" style="left:104px"><h4>OUR COMPANY</h4><ul><li>ABOUT US</li><li>OUR SHOWROOM</li><li>DIRECTIONS</li><li>HOURS OF OPERATION</li><li>MEMBER ACCOUNTS</li><li>CONTACT US</li></ul></div>
  <div class="f-col" style="left:344px"><h4>OUR PRINCIPLES</h4><ul><li>CUSTOMER SATISFACTION</li><li>UNBEATABLE PRICES</li><li>RETURN POLICY</li><li>WARRANTY</li><li>INFORMATION POLICY</li></ul></div>
  <div class="f-col" style="left:614px"><h4>OUR SPECIALTIES</h4><ul><li>DIAMOND BROKERAGE</li><li>ENGAGEMENT RINGS</li><li>WOMEN'S WEDDING BANDS</li><li>MEN'S WEDDING BANDS</li><li>BRACELETS</li><li>EARRINGS</li><li>PENDANTS</li></ul></div>
  <div class="f-col" style="left:903px"><h4>OUR SERVICES</h4><ul><li>EDUCATION</li><li>CONSULTATION</li><li>APPRAISALS</li><li>SALES &amp; CONSIGNMENTS</li><li>INSURANCE</li><li>JEWELRY REPAIR</li></ul></div>

  <div class="social" style="left:95px;background:#3b5ba0" aria-label="Social link"></div>
  <div class="social" style="left:133px;background:#e0533f" aria-label="Social link"></div>
  <div class="social" style="left:171px;background:#38a7e6" aria-label="Social link"></div>
  <div class="social" style="left:209px;background:#e0507a" aria-label="Social link"></div>
  <div class="social" style="left:234px;background:#d8262e;transform:translateX(13px)" aria-label="Social link"></div>
  <div class="social" style="left:269px;background:#d0303a;transform:translateX(12px)" aria-label="Social link"></div>

  <div class="pay" style="left:725px" aria-label="Payment method"></div>
  <div class="pay" style="left:774px" aria-label="Payment method"></div>
  <div class="pay" style="left:823px" aria-label="Payment method"></div>
  <div class="pay" style="left:872px" aria-label="Payment method"></div>
  <div class="pay" style="left:921px" aria-label="Payment method"></div>
  <div class="abs badge" aria-label="Security certificate"></div>

  <div class="abs legal">
    <b>Corwin Hale</b><br>
    At Corwin Hale Inc., buying an engagement ring or wedding band will be a positive piece of the story of your love.<br>
    Get the information you need to find and select the stunning antique, vintage, or replica engagement ring of your sweetheart's dreams.<br>
    Copyright © 1999-2017 Corwin Hale Inc. All rights reserved.
  </div>
</footer>

</body>
</html>
```